Webdesign für  Kranken- und Seniorenpflege
Webdesign für Kranken- und Seniorenpflege
Zielgruppe
Ambulante Kranken- und Seniorenpflege
Tagespflege in Limbach-Oberfrohna, Mittweida und Chemnitz
Palliativpflege
Aufgabenstellung
- Erstellung in Adobe Photoshop
- Orientieren Sie sich am Socialmedia-Auftritt des Kunden

```html
<!DOCTYPE html>
<html lang="de">
<head>
<meta charset="utf-8">
<title>Zeit für Helden – Karriere</title>
<link rel="stylesheet" href="https://fonts.googleapis.com/css2?family=Fira+Sans:wght@400;500;600;700&display=swap">
<style>
  :root {
    --berry: #a2325f;
    --sun: #f1b52e;
    --sun-deep: #e7a21c;
    --sun-soft: #f6c957;
    --white: #ffffff;
    --page: #ffffff;
  }
  * { box-sizing: border-box; margin: 0; padding: 0; }
  html, body {
    width: 1200px;
    height: 800px;
    overflow: hidden;
    background: var(--page);
    font-family: "Fira Sans", Arial, sans-serif;
  }
  .page {
    position: relative;
    width: 1200px;
    height: 800px;
    background: var(--page);
  }
  .site-header {
    height: 120px;
    display: flex;
    align-items: flex-end;
    justify-content: center;
    padding-bottom: 28px;
  }
  .site-title {
    color: var(--berry);
    font-weight: 600;
    font-size: 22px;
    letter-spacing: 0.2px;
  }
  .hero {
    position: relative;
    height: 430px;
    overflow: hidden;
  }
  .hero-photo {
    position: absolute;
    inset: 0;
    background:
      radial-gradient(ellipse at 20% 35%, rgba(196, 122, 60, 0.55), transparent 55%),
      radial-gradient(ellipse at 82% 55%, rgba(150, 70, 55, 0.45), transparent 55%),
      radial-gradient(ellipse at 50% 40%, rgba(205, 140, 70, 0.4), transparent 60%),
      linear-gradient(180deg, var(--sun-deep), var(--sun));
  }
  .hero-content {
    position: relative;
    z-index: 1;
    height: 100%;
    display: flex;
    flex-direction: column;
    align-items: center;
    justify-content: center;
    text-align: center;
    color: var(--white);
    padding-top: 40px;
  }
  .hero-headline {
    font-weight: 700;
    font-size: 36px;
    line-height: 1.2;
    max-width: 860px;
  }
  .hero-lead {
    margin-top: 14px;
    font-weight: 500;
    font-size: 19px;
  }
  .apply-button {
    margin-top: 22px;
    display: inline-block;
    padding: 6px 34px;
    background: var(--white);
    color: var(--berry);
    border-radius: 14px;
    font-weight: 600;
    font-size: 12px;
    text-decoration: none;
  }
  .insights {
    padding-top: 44px;
    text-align: center;
  }
  .insights-title {
    color: var(--berry);
    font-weight: 600;
    font-size: 22px;
  }
  .insight-list {
    list-style: none;
    display: flex;
    justify-content: center;
    gap: 80px;
    margin-top: 36px;
  }
  .insight-item {
    width: 260px;
    color: var(--sun);
    font-weight: 600;
    font-size: 19px;
    line-height: 1.2;
    text-align: left;
  }
</style>
</head>
<body>
<div class="page">
  <header class="site-header">
    <h1 class="site-title">Zeit für Helden</h1>
  </header>

  <section class="hero">
    <div class="hero-photo" role="img" aria-label="Foto eines fröhlichen Pflegeteams in weinroten Poloshirts bei Feiern, mit gelber Farbüberlagerung"></div>
    <div class="hero-content">
      <h2 class="hero-headline">Bereichern Sie unser Unternehmen<br>mit ihrer Fachkompetenzund zögern Sie nicht lange!</h2>
      <p class="hero-lead">Unsere Teams sind aufgeschlossen und mit Freude bei der Arbeit!</p>
      <a class="apply-button" href="#">Jetzt Bewerben</a>
    </div>
  </section>

  <section class="insights">
    <h2 class="insights-title">Aktuelle Einblicke</h2>
    <ul class="insight-list">
      <li class="insight-item">Sommerfest in der Tagespflege „Lindenhof“</li>
      <li class="insight-item">Wochenausklang am Schwanenteich in Mittweida</li>
      <li class="insight-item">Maifest in der Tagespflege „Am Brunnen“</li>
    </ul>
  </section>
</div>
</body>
</html>
```